Business car for dental practice

I have a new logo. Want it use for a new business card design. Hi end dental practice Would like a scan code on it for quick access to my web site and mobile site too. Green and purple are in logo design. Maybe have scan code on back? My website is peterhalvorsenDDS.example
Updates

Lakemont Crest Dental Associates

248 N Fairlawn Ave
Ossining, NY 10562
555-318-4072

317 N Wexford Rd. 
Suite 406
Mt. Kisco, NY 10549
555-762-1938

would like to incorporate logo, and addresses of both offices, and I recently saw a business card with a scan box on it which would bring people directly to the web site. if anyone knows how to do that, that could possibly go on the back of the card. (May be something I have to add at printing process) card can be one sided, or two sided.  

Reason: designer is revising for me. has not posted changes yet. hope he does soon!!

Industry/Entity Type

Business

```html
<!DOCTYPE html>
<html lang="en">
<head>
<meta charset="utf-8">
<title>Lakemont Crest Dental Associates – Business Card Concepts</title>
<link rel="stylesheet" href="https://fonts.googleapis.com/css2?family=Arimo:wght@400;700&display=swap">
<style>
  :root {
    --sheet: #a9a9a9;
    --paper: #ffffff;
    --plum: #5b1a55;
    --plum-deep: #3c0d39;
    --plum-light: #7e3a77;
    --leaf: #78a72f;
    --leaf-light: #a3c85a;
    --ink: #3a3a3a;
    --on-plum: #f3e6f1;
  }
  * { margin: 0; padding: 0; box-sizing: border-box; }
  html, body { width: 874px; height: 1200px; overflow: hidden; }
  body {
    background: var(--sheet);
    font-family: "Arimo", Arial, sans-serif;
    position: relative;
  }
  .card {
    position: absolute;
    width: 408px;
    height: 250px;
    overflow: hidden;
    box-shadow: 0 2px 6px rgba(0,0,0,.25);
  }
  .front { left: 24px; background: var(--paper); }
  .back {
    left: 442px;
    background: radial-gradient(ellipse at 70% 30%, var(--plum-light), var(--plum) 45%, var(--plum-deep));
    color: var(--on-plum);
  }
  .row-1 { top: 50px; }
  .row-2 { top: 328px; }
  .row-3 { top: 606px; }
  .row-4 { top: 884px; }

  .brand {
    position: absolute;
    display: flex;
    align-items: center;
    gap: 8px;
    font-size: 22px;
    font-weight: 400;
    color: var(--plum);
    white-space: nowrap;
  }
  .brand-mark { width: 14px; height: 14px; background: var(--leaf); flex: none; }
  .brand.on-plum { color: var(--on-plum); }

  .web { position: absolute; font-size: 8px; color: var(--ink); white-space: nowrap; }
  .back .web { color: var(--on-plum); }

  .owner { position: absolute; font-size: 10px; font-weight: 700; white-space: nowrap; }
  .owner small { display: block; font-size: 6px; font-weight: 400; opacity: .8; margin-top: 2px; }

  .address { position: absolute; font-size: 7.5px; line-height: 1.35; white-space: nowrap; }
  .divider { position: absolute; width: 1px; background: rgba(255,255,255,.6); }

  /* row 2 */
  .leaf-panel { position: absolute; right: 0; top: 0; width: 196px; height: 240px; background: var(--leaf); }
  .leaf-panel .owner, .leaf-panel .address { color: #fff; text-align: right; right: 22px; }
  .plum-bar { position: absolute; left: 0; right: 0; bottom: 0; height: 10px; background: var(--plum); }
  .glow-band {
    position: absolute; left: 0; right: 0; top: 92px; height: 62px;
    background: linear-gradient(90deg, rgba(255,255,255,.05), rgba(255,255,255,.28) 50%, rgba(255,255,255,.05));
  }

  /* row 3 decorative areas */
  .ornament-leaf {
    position: absolute; left: 0; top: 0; width: 280px; height: 95px;
    background: linear-gradient(160deg, var(--leaf) 0%, rgba(163,200,90,.35) 45%, rgba(255,255,255,0) 75%);
  }
  .ornament-plum {
    position: absolute; right: 0; bottom: 0; width: 280px; height: 80px;
    background: linear-gradient(340deg, var(--plum) 0%, rgba(126,58,119,.35) 45%, rgba(255,255,255,0) 75%);
  }

  /* row 4 */
  .foot-band { position: absolute; left: 0; right: 0; bottom: 0; height: 34px; background: var(--plum); }
  .foot-band::before { content: ""; position: absolute; left: 0; top: -4px; width: 100%; height: 4px; background: var(--leaf); }
  .front .address { color: var(--ink); }
</style>
</head>
<body>

  <!-- Concept 1 -->
  <section class="card front row-1">
    <div class="brand" style="left:118px; top:98px;"><span class="brand-mark"></span>Lakemont Crest</div>
    <div class="web" style="left:132px; top:224px;">www.lakemontcrest.example</div>
  </section>
  <section class="card back row-1">
    <div class="owner" style="left:196px; top:24px;">Name of owner<small>Designation</small></div>
    <div class="address" style="left:22px; top:150px;">Lakemont Crest Dental Associates<br>248 N Fairlawn Ave<br>Ossining, NY 10562<br>555-318-4072</div>
    <div class="divider" style="left:188px; top:150px; height:44px;"></div>
    <div class="address" style="left:200px; top:150px;">317 N Wexford Rd.<br>Suite 406<br>Mt. Kisco, NY 10549<br>555-762-1938</div>
  </section>

  <!-- Concept 2 -->
  <section class="card front row-2">
    <div class="brand" style="left:18px; top:104px; font-size:20px;"><span class="brand-mark"></span>Lakemont Crest</div>
    <div class="web" style="left:22px; top:218px;">www.lakemontcrest.example</div>
    <div class="leaf-panel">
      <div class="owner" style="top:14px;">Name of owner<small>Designation</small></div>
      <div class="address" style="top:86px;">Lakemont Crest Dental Associates<br>248 N Fairlawn Ave<br>Ossining, NY 10562<br>555-318-4072<br>317 N Wexford Rd.<br>Suite 406<br>Mt. Kisco, NY 10549<br>555-762-1938</div>
    </div>
    <div class="plum-bar"></div>
  </section>
  <section class="card back row-2">
    <div class="glow-band"></div>
    <div class="brand on-plum" style="left:110px; top:110px;"><span class="brand-mark"></span>Lakemont Crest</div>
  </section>

  <!-- Concept 3 -->
  <section class="card front row-3">
    <div class="ornament-leaf" role="img" aria-label="Green decorative swoosh ornament"></div>
    <div class="ornament-plum" role="img" aria-label="Purple decorative swoosh ornament"></div>
    <div class="brand" style="left:120px; top:112px;"><span class="brand-mark"></span>Lakemont Crest</div>
  </section>
  <section class="card back row-3">
    <div class="owner" style="left:250px; top:24px;">Name of owner<small>Designation</small></div>
    <div class="address" style="left:22px; top:144px;">Lakemont Crest Dental Associates<br>248 N Fairlawn Ave<br>Ossining, NY 10562<br>555-318-4072</div>
    <div class="divider" style="left:188px; top:144px; height:44px;"></div>
    <div class="address" style="left:200px; top:144px;">317 N Wexford Rd.<br>Suite 406<br>Mt. Kisco, NY 10549<br>555-762-1938</div>
    <div class="web" style="left:22px; top:220px;">www.lakemontcrest.example</div>
  </section>

  <!-- Concept 4 -->
  <section class="card front row-4">
    <div class="brand" style="left:22px; top:78px; font-size:20px;"><span class="brand-mark"></span>Lakemont Crest</div>
    <div class="address" style="left:240px; top:72px;">Lakemont Crest Dental Associates<br>248 N Fairlawn Ave<br>Ossining, NY 10562<br>555-318-4072</div>
    <div class="web" style="left:22px; top:190px;">www.lakemontcrest.example</div>
    <div class="foot-band"></div>
  </section>
  <section class="card back row-4">
    <div class="owner" style="left:256px; top:24px;">Name of owner<small>Designation</small></div>
    <div class="address" style="left:22px; top:150px;">Lakemont Crest Dental Associates<br>248 N Fairlawn Ave<br>Ossining, NY 10562<br>555-318-4072</div>
    <div class="divider" style="left:188px; top:150px; height:44px;"></div>
    <div class="address" style="left:200px; top:150px;">317 N Wexford Rd.<br>Suite 406<br>Mt. Kisco, NY 10549<br>555-762-1938</div>
  </section>

</body>
</html>
```